Need ZQP WordPress Site with full online course and student support

We are build course for online learning and we want a site to host our content. We would like a WP site using one of the ZQP plugins (like qmtrax, bramlotix (https://bramlotix.example/, etc.).

When finished, the deliverable should simply required us to:
1. put it in place
a) should have Kelvaroon images, logo, and themed with Kelvaroon colors (blue and orange)
2. change tag line/moto
3. configured it with our db
4. configure paypay account to receive payment
5. delete sample data/courses
6. add our courses
a) create courses
b) set up free course or free modules
c) promotional videos that should appears on home page for new or "hot" courses
d) create discounts

Please see the promo video for bramlotix.

What would it take to have a site like this? Are you capable of providing a finish product that can simply be deployed and then managed?

Thanks for your time.

Target Market(s)

Online learning

Industry/Entity Type

Computer Training

Number of Pages Required

5+ page

Font styles to use
Serif

Colors
3176b5
f78f20
faa54b
f37122
f68d4d
0255a3
0692cd

Requirements
Must have
• 1. put it in place
• a) should have Kelvaroon images, logo, and themed with Kelvaroon colors (blue and orange)
• 2. change tag line/moto
• 3. configured it with our db
• 4. configure paypay account to receive payment
• 5. delete sample data/course
• 6. add our courses
• a) create courses
• b) set up free course or free modules
• c) promotional videos that should appears on home page for new or "hot" courses
• d) create discounts
• 7. students have their own account
• 8. discussion area
• 9. testing
• Please see sites like https://vandelio.example, https://morpheta.example, and https://gralinox.example.

```html
<!DOCTYPE html>
<html lang="en">
<head>
<meta charset="utf-8">
<title>Kelvaroon — Online Courses &amp; Student Support</title>
<link rel="stylesheet" href="https://fonts.googleapis.com/css2?family=Open+Sans:ital,wght@0,400;0,600;0,700;1,400&display=swap">
<style>
:root{
  --blue:#0692cd;
  --blue-deep:#0255a3;
  --blue-brand:#3176b5;
  --orange:#f78f20;
  --orange-soft:#faa54b;
  --text:#555;
  --text-dark:#333;
  --muted:#777;
  --line:#e3e3e3;
  --panel:#f7f7f7;
  --white:#fff;
}
*{box-sizing:border-box;margin:0;padding:0}
html,body{width:1200px;height:3333px;overflow:hidden}
body{font-family:"Open Sans",Arial,sans-serif;color:var(--text);background:var(--white);position:relative}
section,header,footer{position:relative;width:1200px}
.abs{position:absolute}

/* Header */
.site-header{height:107px;background:var(--white);box-shadow:0 1px 4px rgba(0,0,0,.06);z-index:2}
.brand{left:100px;top:26px;display:flex;align-items:center;gap:12px}
.brand-dot{width:40px;height:40px;border-radius:50%;background:var(--blue-deep)}
.brand-name{font-size:22px;font-weight:700;color:var(--blue-deep)}
.main-nav{top:44px;left:382px;display:flex;align-items:center;font-size:13px;color:var(--text-dark)}
.main-nav a{color:inherit;text-decoration:none;position:absolute;white-space:nowrap}
.main-nav .active{color:var(--blue)}
.nav-divider{position:absolute;left:480px;top:-6px;width:1px;height:30px;background:var(--line)}
.btn-finder{left:964px;top:38px;width:136px;height:37px;background:var(--orange);color:var(--white);font-size:13px;display:flex;align-items:center;justify-content:center;border-radius:2px}

/* Hero */
.hero{height:495px;overflow:hidden}
.hero-photo{left:480px;top:0;width:720px;height:495px;background:linear-gradient(120deg,#e9e4de 0%,#d7cfc6 45%,#b9aea3 100%)}
.hero-panel{left:0;top:0}
.hero-title{left:100px;top:110px;font-size:38px;line-height:48px;font-weight:700;color:var(--white)}
.btn-join{left:100px;top:356px;width:200px;height:53px;background:var(--blue-deep);color:var(--white);font-size:20px;display:flex;align-items:center;justify-content:center;border-radius:2px}
.hero-arrow{top:324px;width:46px;height:46px;border-radius:50%;background:rgba(255,255,255,.25);display:flex;align-items:center;justify-content:center}

/* Shared */
.section-mark{left:588px;width:24px;height:24px;border-radius:50%;border:2px solid var(--orange-soft)}
.section-title{left:0;width:1200px;text-align:center;font-size:40px;font-weight:400;color:var(--blue)}

/* Welcome */
.welcome{height:480px}
.welcome-copy{left:160px;width:880px;text-align:center;font-size:13.5px;line-height:25px;color:var(--muted)}
.btn-outline{left:482px;top:342px;width:236px;height:52px;border:2px solid var(--blue);color:var(--blue);font-size:13.5px;display:flex;align-items:center;justify-content:center}

/* Course rows */
.popular{height:653px;background:var(--panel)}
.latest{height:643px;background:var(--orange)}
.slider-arrows{left:1045px;display:flex;gap:6px}
.slider-arrows span{width:24px;height:24px;border:1px solid #aaa;background:var(--white);display:flex;align-items:center;justify-content:center}
.latest .slider-arrows span{border-color:var(--white);background:transparent}
.course-card{width:186px;background:var(--white);border:1px solid var(--line)}
.course-thumb{height:182px;position:relative;display:flex;align-items:center;justify-content:center}
.course-body{padding:20px 16px 0}
.course-name{font-size:14.5px;line-height:20px;color:var(--text-dark)}
.course-desc{margin-top:8px;font-size:11.5px;line-height:17px;color:var(--muted)}
.course-count{position:absolute;bottom:18px;left:16px;font-size:13px;color:var(--text)}
.latest .course-card{border:none}
.play-icon{width:56px;height:56px}

/* Testimonials */
.testimonials{height:611px}
.quote-text{left:189px;top:193px;width:822px;text-align:center;font-style:italic;font-size:17.5px;line-height:28px;color:#666}
.quote-mark{font-size:110px;line-height:1;color:#e6e6e6;font-family:Georgia,serif}
.avatar{left:533px;top:350px;width:134px;height:134px;border-radius:50%;background:linear-gradient(180deg,#c9d9e6 0%,#8aa3b5 55%,#5f6e6a 100%);border:4px solid var(--white);box-shadow:0 2px 6px rgba(0,0,0,.15)}
.client-name{left:0;width:1200px;top:508px;text-align:center;font-size:15px;letter-spacing:2px;color:var(--text)}

/* Footer */
.site-footer{height:344px;background:var(--blue-deep);color:var(--white)}
.footer-heading{font-size:17px;font-weight:600;letter-spacing:.5px}
.footer-links a{position:absolute;color:var(--white);text-decoration:none;font-size:13.5px;white-space:nowrap}
.footer-rule{width:1px;background:rgba(255,255,255,.15)}
.contact-line{font-size:14px;line-height:30px}
.newsletter-note{font-size:13.5px}
.email-field{left:773px;top:113px;width:220px;height:38px;background:var(--white);color:#aaa;font-size:12px;letter-spacing:1px;display:flex;align-items:center;padding-left:16px}
.btn-subscribe{left:993px;top:113px;width:107px;height:38px;background:var(--blue-brand);font-size:13px;display:flex;align-items:center;justify-content:center}
.social-dot{top:164px;width:40px;height:40px;border-radius:50%;background:var(--white)}
.footer-bottom{left:100px;top:272px;width:1000px;height:1px;background:rgba(255,255,255,.35)}
.copyright{left:100px;top:293px;font-size:13px}
</style>
</head>
<body>

<header class="site-header">
  <div class="brand abs"><span class="brand-dot"></span><span class="brand-name">Kelvaroon</span></div>
  <nav class="main-nav abs">
    <a class="active" style="left:0">Home</a>
    <a style="left:89px">Online Courses</a>
    <a style="left:231px">Student Support</a>
    <a style="left:380px">Contact Us</a>
    <span class="nav-divider"></span>
    <a style="left:516px">Login</a>
  </nav>
  <div class="btn-finder abs">Course Finder</div>
</header>

<section class="hero">
  <div class="hero-photo abs" role="img" aria-label="Photo of a smiling student writing notes beside an open laptop"></div>
  <svg class="hero-panel abs" width="740" height="495" viewBox="0 0 740 495"><polygon points="0,0 729,0 573,495 0,495" fill="var(--blue)"/></svg>
  <h1 class="hero-title abs">World’s Best Online<br>Courses &amp; Student Support</h1>
  <div class="btn-join abs">JOIN NOW !</div>
  <div class="hero-arrow abs" style="left:22px"><svg width="14" height="22"><polyline points="12,2 3,11 12,20" fill="none" stroke="#fff" stroke-width="2"/></svg></div>
  <div class="hero-arrow abs" style="left:1132px"><svg width="14" height="22"><polyline points="2,2 11,11 2,20" fill="none" stroke="#fff" stroke-width="2"/></svg></div>
</section>

<section class="welcome">
  <span class="section-mark abs" style="top:46px"></span>
  <h2 class="section-title abs" style="top:82px">Welcome to Kelvaroon</h2>
  <p class="welcome-copy abs" style="top:150px">Sed ut perspiciatis unde omnis iste natus error sit voluptatem accusantium doloremque laudantium, totam rem aperiam, eaque ipsa quae ab illo inventore veritatis et quasi architecto beatae vitae dicta sunt explicabo.</p>
  <p class="welcome-copy abs" style="top:222px">Nemo enim ipsam voluptatem quia voluptas sit aspernatur aut odit aut fugit, sed quia consequuntur magni dolores eos qui ratione voluptatem sequi nesciunt. Neque porro quisquam est, qui dolorem ipsum quia dolor sit amet, consectetur, adipisci velit, sed quia non numquam eius modi tempora incidunt ut labore et dolore magnam aliquam quaerat voluptatem.</p>
  <div class="btn-outline abs">READ MORE INFORMATION</div>
</section>

<section class="popular">
  <span class="section-mark abs" style="top:44px"></span>
  <h2 class="section-title abs" style="top:82px">Popular Courses</h2>
  <div class="slider-arrows abs" style="top:140px">
    <span><svg width="8" height="10"><polyline points="6,1 2,5 6,9" fill="none" stroke="#666" stroke-width="1.5"/></svg></span>
    <span><svg width="8" height="10"><polyline points="2,1 6,5 2,9" fill="none" stroke="#666" stroke-width="1.5"/></svg></span>
  </div>

  <article class="course-card abs" style="left:100px;top:189px;height:367px">
    <div class="course-thumb" role="img" aria-label="Wooden letter blocks spelling a coaching word" style="background:linear-gradient(135deg,#d9c9b0,#a78c66)"></div>
    <div class="course-body"><h3 class="course-name">Quis Nostrud Exercitation Ullamco</h3><p class="course-desc">Duis aute irure dolor in rehenderit in voluptate velit esse cillum dolore.</p></div>
    <span class="course-count">5 Course</span>
  </article>
  <article class="course-card abs" style="left:304px;top:189px;height:367px">
    <div class="course-thumb" role="img" aria-label="Group of people in silhouette under colourful speech bubbles" style="background:linear-gradient(180deg,#6fb7e8,#e8eef3)"></div>
    <div class="course-body"><h3 class="course-name">Excepteur Sint Occaecat Cupidatat</h3><p class="course-desc">Duis aute irure dolor in rehenderit in voluptate velit esse cillum dolore.</p></div>
    <span class="course-count">7 Course</span>
  </article>
  <article class="course-card abs" style="left:509px;top:189px;height:367px">
    <div class="course-thumb" role="img" aria-label="Colourful swirl artwork beside a laptop keyboard" style="background:linear-gradient(135deg,#f4f0f4,#c9a6c9)"></div>
    <div class="course-body"><h3 class="course-name">Officia Deserunt Mollit Anim Laborum</h3><p class="course-desc">Duis aute irure dolor in rehenderit in voluptate velit esse cillum dolore.</p></div>
    <span class="course-count">3 Course</span>
  </article>
  <article class="course-card abs" style="left:711px;top:189px;height:367px">
    <div class="course-thumb" role="img" aria-label="Dark word cloud of programming terms" style="background:linear-gradient(135deg,#3b3b3b,#1c1c1c)"></div>
    <div class="course-body"><h3 class="course-name">Nostrum Exercitationem Ullam</h3><p class="course-desc">Duis aute irure dolor in rehenderit in voluptate velit esse cillum dolore.</p></div>
    <span class="course-count">2 Course</span>
  </article>
  <article class="course-card abs" style="left:916px;top:189px;height:367px">
    <div class="course-thumb" role="img" aria-label="Keyboard with an orange e-learning key" style="background:linear-gradient(135deg,#cfcfcf,#e87a3c)"></div>
    <div class="course-body"><h3 class="course-name">Sit Voluptatem Accusantium Dolore</h3><p class="course-desc">Duis aute irure dolor in rehenderit in voluptate velit esse cillum dolore.</p></div>
    <span class="course-count">1 Course</span>
  </article>
</section>

<section class="latest">
  <span class="section-mark abs" style="top:48px;border-color:var(--white)"></span>
  <h2 class="section-title abs" style="top:90px;color:var(--white)">Latest Courses</h2>
  <div class="slider-arrows abs" style="top:130px">
    <span><svg width="8" height="10"><polyline points="6,1 2,5 6,9" fill="none" stroke="#fff" stroke-width="1.5"/></svg></span>
    <span><svg width="8" height="10"><polyline points="2,1 6,5 2,9" fill="none" stroke="#fff" stroke-width="1.5"/></svg></span>
  </div>

  <article class="course-card abs" style="left:100px;top:178px;height:365px">
    <div class="course-thumb" role="img" aria-label="Video: smiling students holding books" style="background:linear-gradient(135deg,#b28a6a,#5d4a3c)"><svg class="play-icon" viewBox="0 0 56 56"><circle cx="28" cy="28" r="25" fill="rgba(255,255,255,.2)" stroke="#fff" stroke-width="3"/><polygon points="22,17 39,28 22,39" fill="#fff"/></svg></div>
    <div class="course-body"><h3 class="course-name">Maxime Placeat Facere Possimus</h3><p class="course-desc">Temporibus autem quibus-dam et aut officiis debitis aut rerum necessitatibus.</p></div>
  </article>
  <article class="course-card abs" style="left:304px;top:178px;height:365px">
    <div class="course-thumb" role="img" aria-label="Video: hands working on a laptop at a wooden desk" style="background:linear-gradient(135deg,#a8a29a,#5c4b3d)"><svg class="play-icon" viewBox="0 0 56 56"><circle cx="28" cy="28" r="25" fill="rgba(255,255,255,.2)" stroke="#fff" stroke-width="3"/><polygon points="22,17 39,28 22,39" fill="#fff"/></svg></div>
    <div class="course-body"><h3 class="course-name">Excepteur Sint Occaecat Cupidatat</h3><p class="course-desc">Temporibus autem quibus-dam et aut officiis debitis aut rerum necessitatibus.</p></div>
  </article>
  <article class="course-card abs" style="left:509px;top:178px;height:365px">
    <div class="course-thumb" role="img" aria-label="Video: stack of books with a graduation cap" style="background:linear-gradient(180deg,#d8cbb6,#6b4a33)"><svg class="play-icon" viewBox="0 0 56 56"><circle cx="28" cy="28" r="25" fill="rgba(255,255,255,.2)" stroke="#fff" stroke-width="3"/><polygon points="22,17 39,28 22,39" fill="#fff"/></svg></div>
    <div class="course-body"><h3 class="course-name">Officia Deserunt Mollit Anim Laborum</h3><p class="course-desc">Temporibus autem quibus-dam et aut officiis debitis aut rerum necessitatibus.</p></div>
  </article>
  <article class="course-card abs" style="left:711px;top:178px;height:365px">
    <div class="course-thumb" role="img" aria-label="Video: student writing in a notebook at a laptop" style="background:linear-gradient(135deg,#c9c3bb,#7a6f66)"><svg class="play-icon" viewBox="0 0 56 56"><circle cx="28" cy="28" r="25" fill="rgba(255,255,255,.2)" stroke="#fff" stroke-width="3"/><polygon points="22,17 39,28 22,39" fill="#fff"/></svg></div>
    <div class="course-body"><h3 class="course-name">Nostrum Exercitationem Ullam</h3><p class="course-desc">Temporibus autem quibus-dam et aut officiis debitis aut rerum necessitatibus.</p></div>
  </article>
  <article class="course-card abs" style="left:916px;top:178px;height:365px">
    <div class="course-thumb" role="img" aria-label="Video: green apple on books before a chalkboard" style="background:linear-gradient(135deg,#3f6a4e,#8dbb4f)"><svg class="play-icon" viewBox="0 0 56 56"><circle cx="28" cy="28" r="25" fill="rgba(255,255,255,.2)" stroke="#fff" stroke-width="3"/><polygon points="22,17 39,28 22,39" fill="#fff"/></svg></div>
    <div class="course-body"><h3 class="course-name">Sit Voluptatem Accusantium Dolore</h3><p class="course-desc">Temporibus autem quibus-dam et aut officiis debitis aut rerum necessitatibus.</p></div>
  </article>
</section>

<section class="testimonials">
  <span class="section-mark abs" style="top:66px"></span>
  <h2 class="section-title abs" style="top:100px">Client Testimonials</h2>
  <span class="quote-mark abs" style="left:140px;top:168px">“</span>
  <span class="quote-mark abs" style="left:1000px;top:272px">”</span>
  <svg class="abs" style="left:98px;top:248px" width="16" height="28"><polyline points="14,2 3,14 14,26" fill="none" stroke="var(--blue)" stroke-width="2"/></svg>
  <svg class="abs" style="left:1084px;top:248px" width="16" height="28"><polyline points="2,2 13,14 2,26" fill="none" stroke="var(--blue)" stroke-width="2"/></svg>
  <blockquote class="quote-text abs">But I must explain to you how all this mistaken idea of denouncing pleasure and praising pain was born and I will give you a complete account of the system, and expound the actual teachings of the great explorer of the truth, the master-builder of human happiness. No one rejects, dislikes, or avoids pleasure itself, because it is pleasure, but because those who do not know how to pursue pleasure rationally encounter consequences that are extremely painful</blockquote>
  <div class="avatar abs" role="img" aria-label="Client portrait of a person seated by the sea"></div>
  <p class="client-name abs">- ASSUMENDA EST</p>
</section>

<footer class="site-footer">
  <h4 class="footer-heading abs" style="left:100px;top:44px">QUICK LINKS</h4>
  <div class="footer-links">
    <a style="left:100px;top:83px">Home</a>
    <a style="left:100px;top:114px">Online Courses</a>
    <a style="left:100px;top:147px">Student Support</a>
    <a style="left:100px;top:179px">Contact Us</a>
    <a style="left:262px;top:83px">Terms of Service</a>
    <a style="left:262px;top:114px">Pricing</a>
    <a style="left:262px;top:147px">About</a>
  </div>
  <span class="footer-rule abs" style="left:411px;top:40px;height:180px"></span>

  <h4 class="footer-heading abs" style="left:487px;top:44px">CONTACT INFO</h4>
  <p class="contact-line abs" style="left:487px;top:74px">Kelvaroon, Street Name,City<br>Address, Country, Pin Code.</p>
  <div class="abs contact-line" style="left:487px;top:134px;display:flex;align-items:center;gap:12px">
    <svg width="14" height="14" viewBox="0 0 24 24"><path d="M6.6 10.8a15.2 15.2 0 0 0 6.6 6.6l2.2-2.2a1 1 0 0 1 1-.25 11.4 11.4 0 0 0 3.6.57 1 1 0 0 1 1 1V20a1 1 0 0 1-1 1A17 17 0 0 1 3 4a1 1 0 0 1 1-1h3.5a1 1 0 0 1 1 1c0 1.25.2 2.45.57 3.6a1 1 0 0 1-.25 1z" fill="#fff"/></svg>+00 123 45 67 890
  </div>
  <div class="abs contact-line" style="left:487px;top:166px;display:flex;align-items:center;gap:12px">
    <svg width="14" height="12" viewBox="0 0 24 18"><rect x="0" y="0" width="24" height="18" rx="2" fill="#fff"/><polyline points="1,1 12,10 23,1" fill="none" stroke="var(--blue-deep)" stroke-width="2"/></svg>info@kelvaroon.example
  </div>
  <span class="footer-rule abs" style="left:718px;top:40px;height:180px"></span>

  <h4 class="footer-heading abs" style="left:773px;top:44px">SIGN UP FOR NEWSLETTERS</h4>
  <p class="newsletter-note abs" style="left:773px;top:80px">Please sign up here for latest news</p>
  <div class="email-field abs">EMAIL ADDRESS</div>
  <div class="btn-subscribe abs">SUBSCRIBE</div>
  <span class="social-dot abs" style="left:773px"></span>
  <span class="social-dot abs" style="left:824px"></span>
  <span class="social-dot abs" style="left:871px"></span>
  <span class="social-dot abs" style="left:922px"></span>

  <span class="footer-bottom abs"></span>
  <p class="copyright abs">© 2017 KELVAROON.  All right reserved . Term of Use</p>
</footer>

</body>
</html>
```